Best Seller Cover Design for Inspirational Non-Fiction, Self-Help Book

I've been working diligently on a book title "Quiet Harbor Ascent" that will be pivotal for my coaching business. We're heavily investing in marketing and public relations for this and would love it to be a best seller (every other's dream). I need an amazing book cover design that is eye-catching, description, creative, interesting, and compelling, Can you work your magic?I've attached a detailed description along with the content for the back cover. Please let me know if all the content does not fit and I'm happy to reduce it. I need a cover that sells and speaks to the description, whatever you think that will be best. Book DetailsTitle: Self-Defined SuccessSubtitle: Spoiler Alert: You Already Have Everything It TakesAuthor: Ngan H. NguyenSpecifics:- The book will be 5.5" by 8.5" and 216 pages (may change slightly and we can update the spine in final revisions). - Paperback and leave space for a bar code- Will need the raw files so this can be redesigned into hardcover down the line- Brindlecart book cover upload ready- Final file will also need the front cover only for e-book version- Add profile headshot (attached) to back-cover if space permits.I do not have a clear vision of what will be best for this cover but I really like the evocative style of Warren Kestoly Plenitude book. Thank you!

Target Market(s)

Professionals in transition, aspiring or new entrepreneurs, change-makers.

Font styles to use
Serif
Script

Colors

Designer to choose colors to be used in the design.

Requirements
Must have
• Traditional but with elements that make it interesting and provocative since it is speaking to a twist on a topic that has been well talked about, success.

```html
<!DOCTYPE html>
<html lang="en">
<head>
<meta charset="utf-8">
<title>Quiet Harbor Ascent — Cover Spread</title>
<link href="https://fonts.googleapis.com/css2?family=Oswald:wght@600;700&family=EB+Garamond:wght@400;500;600&family=Questrial&display=swap" rel="stylesheet">
<style>
  :root {
    --backdrop: #e8e8e6;
    --cover: #f6f3c6;
    --cover-glow: #fbf9dc;
    --ink: #3b3f53;
    --body-ink: #3d3d3d;
    --accent-red: #e2452f;
    --spine-edge: #e9e5b4;
    --art-warm: #f3b63f;
    --art-teal: #3fb8b2;
    --art-navy: #2f3447;
    --photo-dark: #4a4440;
    --photo-mid: #7a6a5e;
  }
  * { box-sizing: border-box; margin: 0; padding: 0; }
  html, body { width: 1200px; height: 800px; overflow: hidden; }
  body {
    background: var(--backdrop);
    display: flex;
    align-items: center;
    justify-content: center;
    font-family: "Questrial", sans-serif;
  }
  .cover-spread {
    display: flex;
    height: 720px;
    box-shadow: 0 12px 30px rgba(0,0,0,.18);
  }

  /* Back cover */
  .back-cover {
    width: 466px;
    height: 100%;
    background: var(--cover);
    padding: 38px 40px 0 40px;
    color: var(--body-ink);
  }
  .back-cover__question {
    font-family: "Questrial", sans-serif;
    font-size: 20px;
    line-height: 1.25;
    text-align: center;
    color: #444;
    margin-bottom: 20px;
  }
  .back-cover__blurb p {
    font-size: 11.6px;
    line-height: 1.38;
    text-align: justify;
    margin-bottom: 8px;
  }
  .author-bio {
    margin-top: 20px;
    font-size: 11.6px;
    line-height: 1.4;
    text-align: justify;
  }
  .author-bio__photo {
    float: left;
    width: 86px;
    height: 98px;
    margin: 2px 10px 4px 0;
    background: linear-gradient(160deg, var(--photo-mid), var(--photo-dark));
  }
  .author-bio__name {
    font-weight: 700;
    font-style: italic;
  }

  /* Spine */
  .spine {
    width: 52px;
    height: 100%;
    background: linear-gradient(90deg, var(--spine-edge), var(--cover) 30%, var(--cover) 70%, var(--spine-edge));
    display: flex;
    flex-direction: column;
    align-items: center;
    padding: 56px 0 40px;
    gap: 34px;
  }
  .spine__text {
    writing-mode: vertical-rl;
    color: var(--ink);
    font-family: "Questrial", sans-serif;
    font-weight: 700;
    letter-spacing: 2px;
    font-size: 18px;
    -webkit-text-stroke: .4px var(--ink);
  }
  .spine__author { font-size: 15px; }

  /* Front cover */
  .front-cover {
    width: 466px;
    height: 100%;
    background: radial-gradient(circle at 50% 62%, var(--cover-glow) 0, var(--cover) 45%);
    position: relative;
    color: var(--ink);
  }
  .front-cover__title {
    font-family: "Oswald", sans-serif;
    font-weight: 700;
    text-transform: uppercase;
    text-align: center;
    line-height: .98;
    padding-top: 60px;
  }
  .front-cover__title-top { display: block; font-size: 60px; letter-spacing: 1px; }
  .front-cover__title-main { display: block; font-size: 92px; letter-spacing: 2px; }
  .front-cover__subtitle {
    margin-top: 22px;
    border-top: 1.5px solid var(--accent-red);
    border-bottom: 1.5px solid var(--accent-red);
    padding: 8px 30px 10px;
    font-family: "EB Garamond", serif;
    font-size: 23px;
    line-height: 1.3;
    text-align: center;
    color: #3a3a44;
  }
  .front-cover__art {
    position: absolute;
    left: 118px;
    top: 346px;
    width: 230px;
    height: 290px;
  }
  .front-cover__author {
    position: absolute;
    left: 0; right: 0;
    bottom: 30px;
    text-align: center;
    font-family: "EB Garamond", serif;
    font-weight: 600;
    font-size: 26px;
    letter-spacing: 1px;
    color: #1f1f24;
  }
</style>
</head>
<body>
  <main class="cover-spread">
    <section class="back-cover">
      <h2 class="back-cover__question">When all is said and done,<br>what will matter to you most?</h2>
      <div class="back-cover__blurb">
        <p>Following someone else’s path or society’s definition of “success” doesn’t often lead to personal fulfillment. At the end of the day, we genuinely want to succeed—not live a life defined by others.</p>
        <p>You can achieve anything you desire, and when you aim high for your spark of passion you will succeed. Passion is what awakens the heart, fires the soul, and fills the spirit. It is passion that energizes and sparks the pull forward through all barriers, uncertainty, and challenges.</p>
        <p>On this journey, we are asked to turn inward and search for the invisible, the hidden, and the sacred possibilities in order to claim what is ours in truth. We will then fill that shell with a desire that will ignite its creation.</p>
        <p>May this book serve as your guide on how to evoke this clarity and desire for your most authentic path enabling you to create a vision for your future that will bring you the ultimate sense of fulfillment. In addition, this book will show you the steps to navigate the path forward toward this new dream giving you the opportunity to awaken innate abilities you didn’t know you had that will open the door to success.</p>
      </div>
      <div class="author-bio">
        <div class="author-bio__photo" role="img" aria-label="Author headshot"></div>
        <p><span class="author-bio__name">Thira M.Olsberg</span> has built her platform of a vision-driven life after 10 years of experience working as a business strategy advisor in Summit 500 companies and at Harwell &amp; Partners. Combining her advisory experience with her passion for spiritual principles of success, she now empowers entrepreneurs, change-makers, and leaders to step into their truth and bring their unique vision to life. Enabling them to change their lives, revolutionize their work, create greater impact in the world.</p>
      </div>
    </section>

    <section class="spine">
      <span class="spine__text spine__title">QUIET HARBOR ASCENT</span>
      <span class="spine__text spine__author">THIRA M.OLSBERG</span>
    </section>

    <section class="front-cover">
      <h1 class="front-cover__title">
        <span class="front-cover__title-top">Quiet Harbor</span>
        <span class="front-cover__title-main">Ascent</span>
      </h1>
      <p class="front-cover__subtitle">Plot Reveal: The Compass Was Yours<br>From the Start</p>
      <svg class="front-cover__art" viewBox="0 0 230 290" role="img" aria-label="Light bulb illustration built from small icons of goals, learning, puzzles and growth">
        <defs>
          <radialGradient id="art-fill" cx="50%" cy="40%" r="60%">
            <stop offset="0" stop-color="#f2a24a"/>
            <stop offset=".55" stop-color="#5fb7b0"/>
            <stop offset="1" stop-color="#3b3f53"/>
          </radialGradient>
        </defs>
        <rect x="0" y="0" width="230" height="290" rx="18" fill="url(#art-fill)" opacity=".85"/>
      </svg>
      <p class="front-cover__author">THIRA M.OLSBERG</p>
    </section>
  </main>
</body>
</html>
```